Medical VIP club - small design

Please read the specs in a design brief attached. Also we don't have logo in a Vector format and attaching the only version we have.

Industry/Entity Type

Club

```html
<!DOCTYPE html>
<html lang="en">
<head>
<meta charset="utf-8">
<title>Curavita – VIP Medical Club</title>
<link href="https://fonts.googleapis.com/css2?family=Open+Sans:wght@400;600;700&family=Arimo:wght@400;700&display=swap" rel="stylesheet">
<style>
  :root {
    --backdrop: #7a6548;
    --backdrop-dark: #5e4a30;
    --page: #f2efe9;
    --header-bg: #d5cfc5;
    --nav-top: #2f2426;
    --nav-bottom: #1d1517;
    --nav-text: #d8d2cb;
    --hero-light: #dcc79d;
    --hero-dark: #b8955c;
    --ink: #1a1714;
    --brand: #4d3f33;
    --button: #7a3d12;
    --button-dark: #5a2a0a;
    --button-text: #f1d8b8;
    --dot: #7a5a38;
    --caption-bg: rgba(40, 40, 40, 0.72);
    --footer-bg: #d3cdc2;
    --footer-link: #2b241c;
    --footer-muted: #5b544c;
  }
  * { box-sizing: border-box; margin: 0; padding: 0; }
  html, body { width: 1200px; height: 887px; overflow: hidden; }
  body {
    background: linear-gradient(180deg, #8c7a62 0%, var(--backdrop) 45%, var(--backdrop-dark) 100%);
    font-family: "Arimo", Arial, sans-serif;
    position: relative;
  }
  .page {
    position: absolute; left: 65px; top: 22px; width: 1069px; height: 843px;
    background: var(--page);
    box-shadow: 0 4px 14px rgba(0,0,0,0.35);
  }
  .site-header {
    height: 131px; background: var(--header-bg);
    display: flex; justify-content: space-between; align-items: center;
    padding: 0 30px 0 36px;
  }
  .brand { display: flex; align-items: center; gap: 12px; }
  .brand-mark { width: 30px; height: 30px; border-radius: 50%; background: var(--brand); }
  .brand-name {
    font-family: "Open Sans", sans-serif; font-weight: 700;
    font-size: 50px; color: var(--brand); letter-spacing: -1px;
  }
  .contact { display: flex; align-items: center; gap: 10px; margin-top: -8px; }
  .contact-label { font-size: 15px; color: #4a443d; }
  .contact-phone { font-size: 33px; font-weight: 700; color: var(--ink); line-height: 1; }
  .main-nav {
    height: 38px; background: linear-gradient(180deg, var(--nav-top), var(--nav-bottom));
    border-bottom: 1px dashed #5c4f46;
    display: flex; justify-content: space-between; align-items: center;
    padding: 0 32px;
  }
  .main-nav a {
    color: var(--nav-text); text-decoration: none; font-size: 17.5px;
  }
  .main-nav a.active { color: #fff; }
  .hero { position: relative; height: 327px; display: flex; }
  .hero-photo {
    width: 422px; height: 100%;
    background: linear-gradient(135deg, #d9d2c4 0%, #8d7c62 40%, #2a2a30 70%, #bfb6a4 100%);
  }
  .hero-pointer { position: absolute; left: 422px; top: 143px; }
  .hero-panel {
    flex: 1; background: radial-gradient(ellipse at 35% 35%, var(--hero-light), var(--hero-dark));
    border-left: 3px solid #e8d9b8;
    padding: 44px 60px 0 75px; position: relative;
  }
  .hero-title {
    font-family: "Open Sans", sans-serif; font-weight: 700; font-size: 50px;
    color: #2a1d12; line-height: 1; letter-spacing: -0.5px;
  }
  .hero-text { margin-top: 16px; font-size: 14.6px; line-height: 22px; color: #000; width: 510px; }
  .register-button {
    display: inline-block; margin-top: 30px; padding: 12px 26px;
    background: linear-gradient(180deg, #8a4a1c, var(--button-dark));
    border: 1px solid #4a2208; border-radius: 4px;
    font-family: "Open Sans", sans-serif; font-weight: 700; font-size: 23px;
    color: var(--button-text); text-decoration: none;
  }
  .slider-dots { position: absolute; right: 18px; bottom: 18px; display: flex; gap: 5px; }
  .slider-dots span { width: 17px; height: 17px; border-radius: 50%; background: var(--dot); }
  .slider-dots span.current { background: transparent; border: 2px solid #1a1410; }
  .services { display: flex; gap: 7px; padding: 33px 9px 0; height: 243px; }
  .service-tile { position: relative; width: 205px; height: 179px; }
  .service-photo { position: absolute; inset: 0; }
  .tile-emergency { background: linear-gradient(160deg, #5a6a4a, #8e1414 40%, #3c2a22); }
  .tile-transport { background: linear-gradient(180deg, #f0a020, #d05a10 55%, #2a1a10); }
  .tile-hotel { background: linear-gradient(160deg, #6a4a34, #c8b08e 55%, #3a2a20); }
  .tile-doctors { background: linear-gradient(150deg, #c89a6a, #e8e4de 45%, #3a5a8a); }
  .tile-membership { background: linear-gradient(160deg, #d8d8d8, #a8a8a8 60%, #707070); }
  .service-caption {
    position: absolute; left: 0; right: 0; bottom: 0; height: 43px;
    background: var(--caption-bg); color: #fff; text-align: center;
    font-size: 15.5px; line-height: 15.5px; padding-top: 6px; text-transform: uppercase;
  }
  .site-footer {
    height: 104px; background: var(--footer-bg); border-top: 1px solid #e6e1d8;
    display: flex; justify-content: space-between; padding: 30px 36px 0 33px;
  }
  .footer-nav { display: flex; gap: 0; }
  .footer-nav a { color: var(--footer-link); text-decoration: none; font-size: 13px; margin-right: 33px; }
  .footer-meta { display: flex; align-items: center; gap: 14px; margin-top: 14px; font-size: 11.5px; color: var(--footer-muted); }
  .footer-meta strong { color: #3b342d; }
  .social { display: flex; gap: 5px; }
  .social span { width: 17px; height: 17px; background: #8c857c; border-radius: 2px; }
  .site-footer .brand { margin-top: 6px; }
  .site-footer .brand-mark { width: 22px; height: 22px; }
  .site-footer .brand-name { font-size: 38px; }
</style>
</head>
<body>
<div class="page">
  <header class="site-header">
    <div class="brand">
      <span class="brand-mark"></span>
      <span class="brand-name">Curavita</span>
    </div>
    <div class="contact">
      <svg width="38" height="38" viewBox="0 0 38 38" aria-hidden="true">
        <circle cx="19" cy="19" r="17" fill="none" stroke="#3a332c" stroke-width="2"/>
        <path d="M13 10c-2 2-2 6 1 11s7 8 10 8l2-3-4-3-2 2c-2-1-4-4-5-6l2-2-2-4z" fill="#3a332c"/>
      </svg>
      <div>
        <div class="contact-label">For more information</div>
        <div class="contact-phone">416-555-010</div>
      </div>
    </div>
  </header>

  <nav class="main-nav">
    <a class="active" href="#">HOME</a>
    <a href="#">ABOUT US</a>
    <a href="#">VIP CLUB</a>
    <a href="#">SERVICES</a>
    <a href="#">PACAKGE AND PRICES</a>
    <a href="#">REGISTRATION</a>
    <a href="#">CONTACT</a>
  </nav>

  <section class="hero">
    <div class="hero-photo" role="img" aria-label="Photo of a luxurious hotel lobby with armchairs and pendant lamps"></div>
    <svg class="hero-pointer" width="38" height="40" viewBox="0 0 38 40" aria-hidden="true">
      <polygon points="0,0 38,20 0,40" fill="#1a1410"/>
    </svg>
    <div class="hero-panel">
      <h1 class="hero-title">VIP CLUB</h1>
      <p class="hero-text">Lorem Ipsum is simply dummy text of the printing and typesetting industry. Lorem Ipsum has been the industry's standard dummy text ever since the 1500s, when an unknown printer took a galley of type and scrambled it to make a type specimen book.</p>
      <a class="register-button" href="#">REGISTER NOW!</a>
      <div class="slider-dots"><span class="current"></span><span></span><span></span><span></span><span></span></div>
    </div>
  </section>

  <section class="services">
    <div class="service-tile">
      <div class="service-photo tile-emergency" role="img" aria-label="Photo of a red emergency entrance sign"></div>
      <div class="service-caption">Emergency<br>Service Plan</div>
    </div>
    <div class="service-tile">
      <div class="service-photo tile-transport" role="img" aria-label="Photo of an airplane landing at sunset"></div>
      <div class="service-caption">Transportation<br>Service</div>
    </div>
    <div class="service-tile">
      <div class="service-photo tile-hotel" role="img" aria-label="Photo of a hotel bedroom"></div>
      <div class="service-caption">Hotel<br>Service</div>
    </div>
    <div class="service-tile">
      <div class="service-photo tile-doctors" role="img" aria-label="Photo of a team of doctors reviewing notes"></div>
      <div class="service-caption">Variety<br>of Doctors</div>
    </div>
    <div class="service-tile">
      <div class="service-photo tile-membership" role="img" aria-label="Photo of a membership application form with a pen"></div>
      <div class="service-caption">Becaome<br>a Member</div>
    </div>
  </section>

  <footer class="site-footer">
    <div>
      <nav class="footer-nav">
        <a href="#">Home</a><a href="#">About Us</a><a href="#">Vip Club</a><a href="#">Services</a><a href="#">Pacakge And Prices</a><a href="#">Registration</a><a href="#">Contact</a>
      </nav>
      <div class="footer-meta">
        <span>Copyright © 2010 <strong>Curavita</strong>. All Rights Reserved.</span>
        <div class="social"><span></span><span></span><span></span></div>
      </div>
    </div>
    <div class="brand">
      <span class="brand-mark"></span>
      <span class="brand-name">Curavita</span>
    </div>
  </footer>
</div>
</body>
</html>
```